Business Card Kelda Law llc examples and ideas are attached.

in addition to the logo we need a desription what we do: "Reprsenting students with disabilites obtain services to progress in the public school system."

If you can squeeze it on the fron at the bottom great if not put it on the back

```html
<!DOCTYPE html>
<html lang="en">
<head>
<meta charset="utf-8">
<title>Kelda Law llc – Business Card</title>
<link rel="stylesheet" href="https://fonts.googleapis.com/css2?family=Libre+Baskerville:wght@400;700&family=Lato:wght@400;700&display=swap">
<style>
  :root {
    --navy: #1b3566;
    --gold: #e5a72a;
    --ink: #222222;
    --paper: #ffffff;
    --backdrop: #e9eaee;
    --rule: #2a2a2a;
  }
  * { box-sizing: border-box; margin: 0; padding: 0; }
  html, body { width: 1200px; height: 864px; overflow: hidden; }
  body {
    background: var(--backdrop);
    position: relative;
    font-family: "Libre Baskerville", Georgia, serif;
  }
  .card {
    position: absolute;
    width: 560px;
    height: 320px;
    background: var(--paper);
    box-shadow: 0 6px 20px rgba(0,0,0,0.12);
    overflow: hidden;
  }
  .card--front { left: 320px; top: 92px; }
  .card--back { left: 320px; top: 452px; }

  .brand-square { display: block; background: var(--navy); flex: none; }
  .brand-name {
    font-weight: 700;
    color: var(--navy);
    text-transform: uppercase;
    letter-spacing: 1px;
    white-space: nowrap;
  }

  /* Front */
  .front-brand {
    position: absolute;
    left: 0; right: 0; top: 78px;
    display: flex;
    flex-direction: column;
    align-items: center;
    gap: 18px;
  }
  .front-brand .brand-square { width: 64px; height: 64px; }
  .front-brand .brand-name { font-size: 32px; }
  .mission {
    position: absolute;
    left: 60px; right: 60px; bottom: 30px;
    font-size: 12px;
    line-height: 1.5;
    color: var(--ink);
    text-align: center;
  }

  /* Back */
  .back-brand {
    position: absolute;
    left: 36px; top: 34px;
    display: flex;
    align-items: center;
    gap: 16px;
  }
  .back-brand .brand-square { width: 72px; height: 72px; }
  .identity { display: flex; flex-direction: column; }
  .identity .brand-name { font-size: 26px; line-height: 1.1; }
  .person-name {
    font-size: 19px; font-weight: 700; color: var(--ink);
    text-transform: uppercase; margin-top: 4px;
  }
  .person-role {
    font-size: 11px; color: var(--navy);
    letter-spacing: 1.5px; margin-top: 3px; text-transform: uppercase;
  }
  .practice {
    font-size: 11px; color: var(--ink); margin-top: 4px; line-height: 1.4;
  }
  .phone {
    position: absolute;
    right: 40px; top: 168px;
    display: flex; align-items: center; gap: 6px;
    font-family: "Lato", Arial, sans-serif;
    font-size: 13px; color: var(--ink);
  }
  .phone-icon {
    width: 16px; height: 16px; background: var(--gold);
    display: flex; align-items: center; justify-content: center;
  }
  .divider {
    position: absolute;
    left: 40px; right: 40px; top: 194px;
    height: 1px; background: var(--rule);
  }
  .contact {
    position: absolute;
    left: 40px; top: 204px;
    font-family: "Lato", Arial, sans-serif;
    font-size: 13px; line-height: 1.4; color: var(--ink);
    font-style: normal;
  }
  .stripe { position: absolute; height: 7px; }
  .stripe--gold { left: 0; width: 300px; top: 298px; background: var(--gold); }
  .stripe--navy { left: 300px; right: 0; top: 284px; background: var(--navy); }
</style>
</head>
<body>
  <section class="card card--front" aria-label="Card front">
    <div class="front-brand">
      <span class="brand-square" aria-hidden="true"></span>
      <span class="brand-name">Kelda Law llc</span>
    </div>
    <p class="mission">Representing students with disabilities obtain services to progress in the public school system.</p>
  </section>

  <section class="card card--back" aria-label="Card back">
    <div class="back-brand">
      <span class="brand-square" aria-hidden="true"></span>
      <div class="identity">
        <span class="brand-name">Kelda Law llc</span>
        <span class="person-name">Tobias R Kelda</span>
        <span class="person-role">Attorney at Law</span>
        <p class="practice">Representing Students in Special Education and Related Services</p>
      </div>
    </div>

    <div class="phone">
      <span class="phone-icon" aria-hidden="true">
        <svg width="10" height="10" viewBox="0 0 24 24"><path fill="#fff" d="M6.6 10.8a15.1 15.1 0 0 0 6.6 6.6l2.2-2.2c.3-.3.7-.4 1-.2 1.1.4 2.3.6 3.6.6.6 0 1 .4 1 1V20c0 .6-.4 1-1 1A17 17 0 0 1 3 4c0-.6.4-1 1-1h3.5c.6 0 1 .4 1 1 0 1.3.2 2.5.6 3.6.1.3 0 .7-.2 1z"/></svg>
      </span>
      <span>555 014 2290</span>
    </div>

    <div class="divider"></div>

    <address class="contact">
      1450 Harbor View Rd.<br>
      Brookfield 40217<br>
      toby.keldalaw@mailbox.com<br>
      By Appoint Only
    </address>

    <span class="stripe stripe--gold"></span>
    <span class="stripe stripe--navy"></span>
  </section>
</body>
</html>
```